Dental Office needs Dynamic Wordpress Website Design

We need a a dynamic WordPress website design including SEO. We also need a mobile site. We would like the design to be easy to navigate, simple and modern. We would like to stick with a black, white and purple theme and existing logo and font. We have content and professional photos all ready to go as we would like to proceed asap.

Industry/Entity Type

Dental

```html
<!DOCTYPE html>
<html lang="en">
<head>
<meta charset="utf-8">
<title>Pine Hollow Dental</title>
<link rel="stylesheet" href="https://fonts.googleapis.com/css2?family=PT+Sans:ital,wght@0,400;0,700;1,400&display=swap">
<style>
:root{
  --stage:#000;
  --lavender:#d9d9fd;
  --plum:#6e3a6e;
  --plum-light:#9a6b9a;
  --plum-deep:#5a1f5a;
  --violet:#b862cc;
  --ink:#111;
  --grey-band:#555;
  --page-bg:#f1f1f1;
  --white:#fff;
  --footer:#a9a9a9;
  --footer-bar:#3a3a3a;
  --field:#8e8e8e;
}
*{box-sizing:border-box;margin:0;padding:0}
html,body{width:1200px;height:900px;overflow:hidden;background:var(--stage);font-family:'PT Sans',sans-serif}
.page{position:absolute;left:237px;top:32px;width:663px;height:844px;background:var(--page-bg);overflow:hidden}
.abs{position:absolute}
.header-bg{left:0;top:0;width:663px;height:245px;background:var(--lavender)}
.header-rule{left:0;top:245px;width:663px;height:9px;background:var(--grey-band)}
.logo{left:46px;top:9px;display:flex;align-items:center;gap:6px}
.logo-mark{width:36px;height:36px;background:var(--plum)}
.logo-name{font-size:15px;line-height:14px;color:var(--plum);width:60px}
.logo-tag{left:46px;top:47px;font-size:8px;color:var(--plum)}
.top-contact{left:457px;top:9px;font-size:8px;color:var(--ink);font-weight:700;display:flex;align-items:center;gap:3px}
.follow{left:540px;top:10px;font-size:5.5px;color:var(--ink);display:flex;gap:6px;align-items:center}
.dot{width:5px;height:5px;background:var(--plum-deep);border-radius:50%}
.nav{left:240px;top:29px;width:377px;height:24px;border-radius:3px;background:linear-gradient(#a173a1,#6f3f70);display:flex}
.nav a{color:var(--white);font-size:8.5px;text-decoration:none;display:flex;align-items:center;justify-content:center;border-right:1px solid rgba(255,255,255,.25);height:100%}
.nav a:last-child{border-right:0}
.hero{left:46px;top:61px;width:571px;height:242px;border-radius:3px;background:linear-gradient(90deg,#4b4b4b,#262626 35%,#1f1f1f)}
.hero-divider{left:227px;top:12px;width:2px;height:218px;background:#555}
.hero-title{left:35px;top:40px;font-size:20px;line-height:21px;color:var(--white);font-weight:700;letter-spacing:.5px}
.hero-text{left:35px;top:89px;width:130px;font-size:7.5px;line-height:9.8px;color:#eee}
.btn{display:inline-flex;align-items:center;justify-content:center;background:linear-gradient(#8a3f8a,var(--plum-deep));color:var(--white);font-size:7.5px;font-weight:700;border-radius:2px}
.hero .btn{position:absolute;left:35px;top:175px;width:67px;height:19px}
.hero-photo{left:194px;top:12px;width:366px;height:218px;background:linear-gradient(135deg,#d7dde3,#a7b5bd 50%,#5c7b6b)}
.panel-purple{background:var(--plum-light);border-radius:3px;color:var(--white)}
.why{left:46px;top:316px;width:183px;height:131px}
.panel-title{font-size:12.5px;font-weight:700;letter-spacing:.4px}
.why .panel-title{position:absolute;left:18px;top:13px}
.why p{position:absolute;left:18px;top:39px;width:148px;font-size:7px;line-height:9.7px}
.director{left:240px;top:316px;width:377px;height:131px;border-radius:3px;background:linear-gradient(#fff,#dcdcdc);border:1px solid #ddd}
.director .panel-title{position:absolute;left:18px;top:11px;color:var(--ink)}
.director p{position:absolute;left:18px;top:38px;width:340px;font-size:7px;line-height:9.6px;color:#333}
.director .btn{position:absolute;left:18px;top:94px;width:67px;height:19px}
.white-band{left:0;top:458px;width:663px;height:125px;background:var(--white)}
.booking{left:46px;top:471px;width:183px;height:102px}
.booking .panel-title{position:absolute;left:18px;top:12px}
.booking svg{position:absolute;left:16px;top:35px}
.booking p{position:absolute;left:68px;top:37px;width:90px;font-size:7px;line-height:9.5px}
.booking .btn{position:absolute;left:68px;top:61px;width:67px;height:18px}
.testi-title{left:240px;top:482px;font-size:12.5px;font-weight:700;color:var(--ink)}
.avatar{left:241px;top:508px;width:48px;height:48px;background:#aaa;border:1px solid #ccc}
.testi-text{left:296px;top:507px;width:320px;font-size:7px;line-height:9.6px;font-style:italic;color:#222}
.testi-name{left:296px;top:537px;font-size:7px;font-weight:700;font-style:italic;color:#222}
.testi-date{left:296px;top:547px;font-size:6px;font-style:italic;color:#777}
.fac-line{top:599px;height:1px;background:#d3d3d3;width:240px}
.fac-title{left:0;width:663px;top:590px;text-align:center;font-size:13px;font-weight:700;color:var(--plum-deep)}
.fac-card{top:613px;width:183px;height:104px;border-radius:3px;overflow:hidden;background:linear-gradient(135deg,#ddd,#8c8c8c)}
.fac-card span{position:absolute;left:0;bottom:0;width:100%;height:27px;background:var(--violet);color:var(--white);font-size:9px;display:flex;align-items:center;justify-content:center}
.footer{left:0;top:727px;width:663px;height:102px;background:var(--footer)}
.foot-name{left:46px;top:12px;font-size:8px;line-height:8px;color:#333;width:50px}
.foot-small{left:46px;top:40px;font-size:5px;line-height:7px;color:#222}
.foot-follow{left:46px;top:62px;font-size:5.5px;color:#222}
.foot-icons{left:46px;top:74px;display:flex;gap:7px}
.foot-icons i{width:5px;height:5px;border-radius:50%;background:#333;display:block}
.foot-head{top:12px;font-size:9px;font-weight:700;color:#111;letter-spacing:.3px}
.foot-about{left:141px;top:33px;width:62px;font-size:6.5px;line-height:9.5px;font-style:italic;color:#333}
.foot-about em{color:var(--violet)}
.foot-loc{left:263px;top:33px;font-size:6.5px;line-height:9.6px;color:#222}
.field{background:var(--field);border-radius:2px;font-size:5px;font-style:italic;color:#ddd;padding:3px 4px}
.send{left:587px;top:69px;width:29px;height:12px;font-size:6px}
.bottom-bar{left:0;top:829px;width:663px;height:15px;background:var(--footer-bar);color:#ddd;font-size:5.5px}
.bottom-bar span{position:absolute;top:4px}
</style>
</head>
<body>
<div class="page">
  <div class="abs header-bg"></div>
  <div class="abs header-rule"></div>

  <div class="abs logo"><div class="logo-mark"></div><div class="logo-name">Pine Hollow Dental</div></div>
  <div class="abs logo-tag">family &amp; cosmetic dentistry</div>

  <div class="abs top-contact">
    <svg width="8" height="8" viewBox="0 0 10 10"><path d="M2 1l2 0 1 2.5-1.3 1a6 6 0 0 0 2.8 2.8l1-1.3L10 7v2c0 .6-.5 1-1 1A9 9 0 0 1 0 2c0-.5.4-1 1-1z" fill="#3a2a4a"/></svg>
    +00 00000000
  </div>
  <div class="abs follow">Follow Us <i class="dot"></i><i class="dot"></i><i class="dot"></i><i class="dot"></i></div>

  <nav class="abs nav">
    <a style="width:60px">Home</a><a style="width:62px">About Us</a><a style="width:67px">Treatments</a><a style="width:68px">Facilities</a><a style="width:52px">Gallery</a><a style="width:68px">Contacts</a>
  </nav>

  <section class="abs hero">
    <div class="abs hero-divider"></div>
    <h1 class="abs hero-title">Lorem ipsum<br>dolor</h1>
    <p class="abs hero-text">Dummy text of the printing and typesetting industry. Lorem Ipsum has been the industry's standard dummy text ever since the 1500s, when an unknown printer took a galley of type and...</p>
    <span class="btn">Read More</span>
    <div class="abs hero-photo" role="img" aria-label="Dentist treating a patient in the dental chair"></div>
  </section>

  <section class="abs panel-purple why">
    <h2 class="panel-title">Why Linden</h2>
    <p>Dummy text of the printing and type-setting industry. Lorem Ipsum has been the industry's standard dummy text vever since the 1500s, when an un-known printer took a galook.dard dummy text ever since the 1500s, when an unknown.</p>
  </section>

  <section class="abs director">
    <h2 class="panel-title">Director's message</h2>
    <p>Dummy text of the printing and typesetting industry. Lorem Ipsum has been the industry's standard dummy text vever since the 1500s, when an unknown printer took a galook.dard dummy text ever since the 1500s, when an unknown printer took a galook.ustry's standard dummy text vever since the 1500s, when an unknown printer took a galook.dard dummy text ever since the 1500s, when an unknown printer took a galook.</p>
    <span class="btn">Read More</span>
  </section>

  <div class="abs white-band"></div>

  <section class="abs panel-purple booking">
    <h2 class="panel-title">Booking</h2>
    <svg width="46" height="46" viewBox="0 0 46 46" fill="none" stroke="#fff" stroke-width="2.5">
      <rect x="2" y="5" width="28" height="28" rx="2"/>
      <line x1="9" y1="1" x2="9" y2="8"/><line x1="23" y1="1" x2="23" y2="8"/>
      <line x1="2" y1="12" x2="30" y2="12"/>
      <circle cx="31" cy="31" r="11" fill="#9a6b9a"/>
      <polyline points="31,25 31,31 36,33"/>
    </svg>
    <p>Advanced Booking is available.</p>
    <span class="btn">Book Now</span>
  </section>

  <h2 class="abs testi-title">Testimonials</h2>
  <div class="abs avatar" role="img" aria-label="Placeholder portrait of the reviewer"></div>
  <p class="abs testi-text">Dummy text of the printing and typesetting industry. Lorem Ipsum has been the industry's standard dummy text vever since the 1500s, when an unknown printer took a galook.dard dummy text ever since the 1500s look a galook.</p>
  <p class="abs testi-name">Aaron Mills</p>
  <p class="abs testi-date">12/04/2014</p>

  <div class="abs fac-line" style="left:46px"></div>
  <div class="abs fac-line" style="left:377px"></div>
  <h2 class="abs fac-title">Facilities</h2>
  <div class="abs fac-card" style="left:46px" role="img" aria-label="Treatment room with dental chair"><span>Lorem ipsum dolor sit amet</span></div>
  <div class="abs fac-card" style="left:240px" role="img" aria-label="Dental operatory with equipment"><span>Lorem ipsum dolor sit amet</span></div>
  <div class="abs fac-card" style="left:434px" role="img" aria-label="Clinic room with dental unit"><span>Lorem ipsum dolor sit amet</span></div>

  <footer class="abs footer">
    <div class="abs foot-name">Pine Hollow Dental</div>
    <div class="abs foot-small">© Privacy Policy<br>All Rights Reserved</div>
    <div class="abs foot-follow">Follow Us</div>
    <div class="abs foot-icons"><i></i><i></i><i></i><i></i></div>

    <h3 class="abs foot-head" style="left:141px">About Pine Hollow</h3>
    <p class="abs foot-about">Dummy text of the print-ing and typesetting indus-try. Lorem Ipsum has been the...<em>[Read more]</em></p>

    <h3 class="abs foot-head" style="left:263px">Location</h3>
    <p class="abs foot-loc">City address goes here<br>City name<br>Zip code, State.<br>Tel : 00 00000000<br>Fax : 0000000000</p>

    <h3 class="abs foot-head" style="left:383px">Send Message</h3>
    <div class="abs field" style="left:383px;top:33px;width:113px;height:13px">Name</div>
    <div class="abs field" style="left:383px;top:51px;width:113px;height:13px">E-mail</div>
    <div class="abs field" style="left:383px;top:69px;width:113px;height:13px">Subject</div>
    <div class="abs field" style="left:504px;top:33px;width:113px;height:30px">Message</div>
    <span class="abs btn send">Send</span>
  </footer>

  <div class="abs bottom-bar"><span style="right:46px">www.example.com</span></div>
</div>
</body>
</html>
```